Tarnwick Professional Services Website

Small website for company presence and information. Company is an IT/Telecom services company. We provide presales and installation services. Included are various company logos including color levels. Site doesn't have to use these exact colors in the logos, but should be complimentary if using different colors. It should have a professional business appearance.
Updates

My apologies for not being more responsive on the designs that have been submitted. I will be narrowing down the submissions and providing additional feedback next week. Thank you for your patience.

Project Deadline Extended
Reason: Sorry again for delays on picking designs. Work has me very busy and I've just not had the time to devote to this project. I am extending the design deadline for a few more days to give me time to make my final decisions. Thank you all for your patience. Stay tuned....

Target Market(s)

Telecom sales companies that sell Brintel telecom products.

Industry/Entity Type

Professional Service

Coding

Coded - Design and coding required

Number of Pages Required

5+ page

Font styles to use
Sans Serif

Colors
3276b5
0355a3
85abd2
85cae6
33a6d7
0692cd
ffffff

Requirements
Must have
• Professional design reflective of IT/Telecom business. A good reference website would be: http://www.quollanetworks.example/. Looking for something similar in function and presence.
Nice to have
• Rolling photos highlighting our services. Traditional navigation across the top of all pages.
Should not have
• No motion video, flashy presentation or overly confused interface.

```html
<!DOCTYPE html>
<html lang="en">
<head>
<meta charset="utf-8">
<title>Tarnwick Professional Services</title>
<link rel="stylesheet" href="https://fonts.googleapis.com/css2?family=Exo+2:ital,wght@0,600;0,700;1,700&family=Lato:wght@400;700&display=swap">
<style>
:root{
  --blue:#0355a3;
  --blue-mid:#3276b5;
  --blue-light:#85abd2;
  --sky:#33a6d7;
  --ink:#111111;
  --text:#333333;
  --muted:#666666;
  --rule:#d6d6d6;
  --panel:#f1f1f1;
  --footer:#1b1f28;
  --white:#ffffff;
  --head:"Exo 2",sans-serif;
  --body:"Lato",sans-serif;
}
*{box-sizing:border-box;margin:0;padding:0}
html,body{width:1200px;height:2332px;overflow:hidden;background:var(--white)}
body{position:relative;font-family:var(--body);color:var(--text)}
.abs{position:absolute}

/* header */
.site-header{position:absolute;left:0;top:0;width:1200px;height:107px;border-top:2px solid var(--blue);background:var(--white)}
.brand{position:absolute;left:98px;top:30px;display:flex;align-items:center;gap:14px}
.brand-mark{width:46px;height:46px;background:var(--blue)}
.brand-name{font-family:var(--head);font-weight:700;font-size:20px;color:var(--blue);letter-spacing:.4px;line-height:21px;width:240px}
.top-tab{position:absolute;left:793px;top:0;width:307px;height:38px;background:var(--blue);clip-path:polygon(0 0,100% 0,96% 100%,4% 100%);display:flex;align-items:center;padding-left:40px;gap:10px;color:var(--white);font-size:15px}
.top-tab .socials{margin-left:auto;margin-right:28px;display:flex;gap:10px}
.top-tab .socials span{width:22px;height:22px;border-radius:50%;border:2px solid var(--white)}
.main-nav{position:absolute;top:68px;left:0;width:1200px;font-family:var(--head);font-weight:700;font-size:12px;color:var(--ink);letter-spacing:.3px}
.main-nav a{position:absolute;transform:translateX(-50%);color:inherit;text-decoration:none;white-space:nowrap}
.main-nav a.active{color:var(--blue)}
.main-nav .sep{position:absolute;top:2px;width:1px;height:12px;background:#999}

/* hero */
.hero{position:absolute;left:0;top:107px;width:1200px;height:513px;background:linear-gradient(90deg,#3d4148 0%,#7d838b 45%,#5b6470 70%,#2e3540 100%)}
.hero-title{position:absolute;left:100px;top:200px;font-family:var(--head);font-style:italic;font-weight:700;font-size:28px;line-height:40px;color:var(--white);letter-spacing:1px;white-space:nowrap}
.hero-arrow{position:absolute;top:230px;width:56px;height:56px;border-radius:50%;border:3px solid rgba(255,255,255,.35);background:rgba(0,0,0,.25)}
.hero-dots{position:absolute;left:570px;top:471px;display:flex;gap:6px}
.hero-dots span{width:12px;height:12px;border-radius:50%;border:1.5px solid var(--white)}
.hero-dots span.on{background:var(--sky)}

/* welcome */
.welcome-kicker{position:absolute;left:100px;top:666px;font-family:var(--head);font-weight:600;font-size:25px;color:var(--ink)}
.welcome-title{position:absolute;left:100px;top:694px;font-family:var(--head);font-weight:700;font-size:35px;color:var(--blue);letter-spacing:.6px;white-space:nowrap}
.welcome-rule{position:absolute;left:100px;top:746px;width:645px;height:1px;background:var(--rule)}
.welcome-copy{position:absolute;left:100px;top:760px;width:645px;font-size:12.5px;line-height:26.5px;color:var(--text)}
.btn{display:inline-block;background:var(--blue);color:var(--white);font-size:13px;text-align:center;border-radius:2px}
.welcome-btn{position:absolute;left:100px;top:960px;width:118px;height:36px;line-height:36px}

.contact-card{position:absolute;left:783px;top:673px;width:318px;height:322px;background:var(--white);box-shadow:0 2px 6px rgba(0,0,0,.2)}
.contact-card h2{height:59px;line-height:59px;background:var(--blue);color:var(--white);text-align:center;font-family:var(--head);font-weight:700;font-size:25px}
.field{position:absolute;height:38px;border:1px solid #cfcfcf;border-radius:2px;font-size:11px;color:#777;padding:11px 9px}
.submit{position:absolute;left:19px;top:262px;width:280px;height:35px;line-height:35px}

/* services */
.services{position:absolute;left:0;top:1049px;width:1200px;height:524px;background:var(--panel)}
.section-title{font-family:var(--head);font-weight:700;font-size:32px;color:var(--ink);letter-spacing:.5px}
.section-title em{font-style:normal;color:var(--blue)}
.divider{position:absolute;height:1px;background:#c9c9c9}
.divider-mark{position:absolute;width:14px;height:14px;background:#888}
.service-card{position:absolute;top:144px;width:232px;height:327px;background:var(--white);border:1px solid #dcdcdc;text-align:center}
.service-photo{margin:4px;height:139px}
.service-card h3{margin-top:22px;font-family:var(--head);font-weight:700;font-size:19px;color:var(--blue)}
.service-card p{margin:10px auto 0;width:200px;font-size:12.5px;line-height:17px;color:var(--text)}
.service-card .btn{margin-top:14px;width:112px;height:32px;line-height:32px}
.side-arrow{position:absolute;top:215px}

/* events & testimonials */
.pager{position:absolute;display:flex;gap:6px}
.pager span{width:24px;height:24px;border-radius:50%;border:1px solid #bbb}
.event{position:absolute;left:100px;width:470px;height:100px}
.event-date{position:absolute;left:0;top:0;width:60px;height:80px;background:var(--blue);border-radius:4px;color:var(--white);text-align:center;font-family:var(--head);font-weight:700}
.event-date b{display:block;font-size:25px;line-height:36px;margin-top:2px}
.event-date i{display:block;font-style:normal;font-size:12px;line-height:15px}
.event-body{position:absolute;left:78px;top:0;width:392px;font-size:12px;line-height:16px}
.event-body strong{display:block;color:var(--ink);font-size:12.5px;line-height:19px;white-space:nowrap}
.testimonial{position:absolute;left:626px;top:1708px;width:474px;height:178px;background:#efefef;border-radius:4px}
.testimonial p{position:absolute;left:20px;top:20px;width:436px;font-style:italic;font-size:12.5px;line-height:25px;color:#555;text-align:justify;text-indent:60px}
.testimonial-tail{position:absolute;left:52px;top:176px}
.testimonial-name{position:absolute;left:746px;top:1900px;font-family:var(--head);font-style:italic;font-weight:700;font-size:17px;color:#555}
.testimonial-photo{position:absolute;left:992px;top:1850px;width:80px;height:88px;border:3px solid var(--white);box-shadow:0 0 3px rgba(0,0,0,.3);background:linear-gradient(180deg,#9fb8cf,#5d7894)}

/* footer */
.site-footer{position:absolute;left:0;top:1989px;width:1200px;height:295px;background:var(--footer);color:#d9d9d9}
.footer-head{position:absolute;top:46px;font-family:var(--head);font-weight:700;font-size:18px;color:var(--white)}
.footer-head em{font-style:normal;color:var(--blue-mid)}
.footer-rule{position:absolute;top:76px;height:1px;background:#3a404c}
.quick-links{position:absolute;left:100px;top:98px;list-style:none;font-size:12.5px;line-height:31px}
.contact-info{position:absolute;left:286px;top:98px;font-size:14px;line-height:19px;color:#e5e5e5}
.contact-info strong{display:block;font-family:var(--head);font-size:15px;color:var(--white)}
.contact-line{display:flex;align-items:center;gap:12px;font-size:12.5px;height:29px}
.map{position:absolute;left:579px;top:98px;width:299px;height:147px;background:linear-gradient(135deg,#e8e2c6,#c9d7e6 55%,#e4d8a8);border:2px solid var(--white)}
.footer-brand{position:absolute;left:926px;top:68px;width:190px;text-align:center}
.footer-brand .mark{width:48px;height:48px;margin:0 auto 12px;background:#c8c8c8}
.footer-brand .name{font-family:var(--head);font-weight:700;font-size:19px;line-height:22px;color:#c8c8c8}
.footer-socials{display:flex;justify-content:center;gap:12px;margin-top:26px}
.footer-socials span{width:28px;height:28px;border-radius:50%;border:2px solid var(--white)}
.copyright{position:absolute;left:0;top:2284px;width:1200px;height:48px;line-height:48px;background:var(--blue);color:var(--white);font-size:14px;text-align:center}
</style>
</head>
<body>

<header class="site-header">
  <div class="brand"><span class="brand-mark"></span><span class="brand-name">Tarnwick<br>Professional Services</span></div>
  <div class="top-tab">
    <svg width="18" height="18" viewBox="0 0 24 24" aria-hidden="true"><path fill="#fff" d="M6.6 10.8a15 15 0 0 0 6.6 6.6l2.2-2.2a1 1 0 0 1 1-.25 11.4 11.4 0 0 0 3.6.57 1 1 0 0 1 1 1V20a1 1 0 0 1-1 1A17 17 0 0 1 3 4a1 1 0 0 1 1-1h3.5a1 1 0 0 1 1 1c0 1.25.2 2.450.57 3.57a1 1 0 0 1-.25 1z"/></svg>
    <span>(555) 014-2290</span>
    <span class="socials"><span></span><span></span><span></span></span>
  </div>
  <nav class="main-nav">
    <a class="active" style="left:522px">HOME</a>
    <span class="sep" style="left:567px"></span>
    <a style="left:653px">COMPANY PROFILE</a>
    <span class="sep" style="left:737px"></span>
    <a style="left:814px">OUR SERVICES</a>
    <span class="sep" style="left:888px"></span>
    <a style="left:942px">EVENTS</a>
    <span class="sep" style="left:995px"></span>
    <a style="left:1058px">CONTACT US</a>
  </nav>
</header>

<section class="hero" role="img" aria-label="Businessman holding a phone with a glowing world network map">
  <h1 class="hero-title">WELCOME TO<br>TARNWICK PROFESSIONAL<br>SERVICES</h1>
  <span class="hero-arrow" style="left:30px"><svg width="50" height="50" viewBox="0 0 50 50"><path d="M29 15 19 25l10 10" fill="none" stroke="#fff" stroke-width="2"/></svg></span>
  <span class="hero-arrow" style="left:1114px"><svg width="50" height="50" viewBox="0 0 50 50"><path d="m21 15 10 10-10 10" fill="none" stroke="#fff" stroke-width="2"/></svg></span>
  <div class="hero-dots"><span></span><span class="on"></span><span></span><span></span></div>
</section>

<main>
  <h2 class="welcome-kicker">Welcome To</h2>
  <h2 class="welcome-title">TARNWICK PROFESSIONAL SERVICES</h2>
  <div class="welcome-rule"></div>
  <p class="welcome-copy">Lorem ipsum dolor sit amet, consectetuer adipiscing elit, sed diam nonummy nibh euismod tincidunt ut laoreet dolore magna aliquam erat volutpat. Ut wisi enim ad minim veniam, quis nostrud exerci tation ullamcorper st lobortis nisl ut aliquip ex ea commodo consequat. Duis autem vel eum iriure dolor in hendrerit in vulp velit es molestie consequat, vel illum dolore eu feugiat nulla facilisis at vero eros et accumsan et iusto odio dignissim qui blandit praesent luptatum zzril delenit augue duis dolore te feugait nulla facilisi. Lorem ipsum dolor sit amet, consectetuer adipiscing elit, sed diam nonummy nibh euismod tincidunt ut laoreet dolore magna aliqua volutpat. Ut wisi enim ad minim veniam, quis nostrud exerci tation ullamcorper.</p>
  <span class="btn welcome-btn">LEARN MORE</span>

  <form class="contact-card">
    <h2>CONTACT US</h2>
    <span class="field" style="left:19px;top:78px;width:137px">Name</span>
    <span class="field" style="left:164px;top:78px;width:135px">Phone</span>
    <span class="field" style="left:19px;top:126px;width:137px">Email</span>
    <span class="field" style="left:164px;top:126px;width:135px">Company</span>
    <span class="field" style="left:19px;top:174px;width:280px;height:74px">Comments</span>
    <span class="btn submit">SUBMIT</span>
  </form>

  <section class="services">
    <h2 class="section-title abs" style="left:0;width:1200px;top:42px;text-align:center">OUR <em>SERVICES</em></h2>
    <span class="divider" style="left:100px;top:103px;width:480px"></span>
    <span class="divider-mark" style="left:593px;top:96px"></span>
    <span class="divider" style="left:620px;top:103px;width:480px"></span>

    <svg class="side-arrow" style="left:45px" width="36" height="66" viewBox="0 0 36 66"><path d="M33 2 3 33l30 31" fill="none" stroke="#777" stroke-width="2"/></svg>
    <svg class="side-arrow" style="left:1116px" width="36" height="66" viewBox="0 0 36 66"><path d="m3 2 30 31L3 64" fill="none" stroke="#777" stroke-width="2"/></svg>

    <article class="service-card" style="left:98px">
      <div class="service-photo" role="img" aria-label="Businessman drawing cloud computing icons" style="background:linear-gradient(135deg,#1d3e63,#3f6f9a)"></div>
      <h3>Managed Services</h3>
      <p>Lorem ipsum dolor sit amet, consectetuer adipiscing elit, sed diam nonummy nibh...</p>
      <span class="btn">LEARN MORE</span>
    </article>
    <article class="service-card" style="left:355px">
      <div class="service-photo" role="img" aria-label="Group of people holding question mark cards" style="background:linear-gradient(180deg,#d9dde2,#8fb2d2)"></div>
      <h3>Readiness Assessment</h3>
      <p>Lorem ipsum dolor sit amet, consectetuer adipiscing elit, sed diam nonummy nibh...</p>
      <span class="btn">LEARN MORE</span>
    </article>
    <article class="service-card" style="left:612px">
      <div class="service-photo" role="img" aria-label="Hand touching a tablet with network lines" style="background:linear-gradient(180deg,#4f5760,#2f8fd0)"></div>
      <h3>Refurbish &amp; Buyback</h3>
      <p>Lorem ipsum dolor sit amet, consectetuer adipiscing elit, sed diam nonummy nibh...</p>
      <span class="btn">LEARN MORE</span>
    </article>
    <article class="service-card" style="left:869px">
      <div class="service-photo" role="img" aria-label="Hands joining puzzle pieces" style="background:linear-gradient(135deg,#3a3a3a,#9c9c9c)"></div>
      <h3>Implementation</h3>
      <p>Lorem ipsum dolor sit amet, consectetuer adipiscing elit, sed diam nonummy nibh...</p>
      <span class="btn">LEARN MORE</span>
    </article>
  </section>

  <h2 class="section-title abs" style="left:99px;top:1614px">EVENTS <em>NEWS</em></h2>
  <div class="pager" style="left:515px;top:1625px"><span></span><span></span></div>
  <span class="divider-mark" style="left:103px;top:1669px"></span>
  <span class="divider" style="left:134px;top:1676px;width:440px"></span>

  <article class="event" style="top:1705px">
    <div class="event-date"><b>22</b><i>JAN</i><i>2017</i></div>
    <div class="event-body"><strong>Lorem ipsum dolor sit amet, consectetuer adipiscing elit<br>Wisi enim and minim.</strong>Sed diam nonummy nibh euismod tincidunt ut laoreet dolore magna aliquam erat volutpat. Ut wisi enim ad minim veniam, quis nostrud exerci tation ullamcorper st lobortis nisl ut aliquip.</div>
  </article>
  <span class="divider" style="left:100px;top:1811px;width:470px;background:#e2e2e2"></span>
  <article class="event" style="top:1826px">
    <div class="event-date"><b>22</b><i>JAN</i><i>2017</i></div>
    <div class="event-body"><strong>Lorem ipsum dolor sit amet, consectetuer adipiscing elit<br>Wisi enim and minim.</strong>Sed diam nonummy nibh euismod tincidunt ut laoreet dolore magna aliquam erat volutpat. Ut wisi enim ad minim veniam, quis nostrud exerci tation ullamcorper st lobortis nisl ut aliquip.</div>
  </article>

  <h2 class="section-title abs" style="left:621px;top:1614px">CLIENT <em>TESTIMONIALS</em></h2>
  <div class="pager" style="left:1040px;top:1625px"><span></span><span></span></div>
  <span class="divider-mark" style="left:626px;top:1669px"></span>
  <span class="divider" style="left:656px;top:1676px;width:444px"></span>

  <blockquote class="testimonial">
    <p>Fusce elementum, nulla vel pellentes consequat, ante nulla hendrerit arcu, ac tincidunt mauris lacus sed leo. vamus suscipit molestie vestibulum. Lorem ipsum dolor sit amet, Fusce elementum, nulla vel pellentes consequat, ante nulla hendrerit arcu, ac tincidunt mauris lacus sed leo. vamus suscipit molestie vestibulum.</p>
    <svg class="testimonial-tail" width="40" height="30" viewBox="0 0 40 30"><path d="M0 0h40L30 30z" fill="#efefef"/></svg>
  </blockquote>
  <span class="testimonial-name">-Nulla vel pellentes</span>
  <span class="testimonial-photo" role="img" aria-label="Portrait photo of the client"></span>
</main>

<footer class="site-footer">
  <h3 class="footer-head" style="left:100px">QUICK <em>LINKS</em></h3>
  <span class="footer-rule" style="left:100px;width:137px"></span>
  <ul class="quick-links">
    <li>• Home</li><li>• Company Profile</li><li>• Our Services</li><li>• Events</li><li>• Contact Us</li>
  </ul>

  <h3 class="footer-head" style="left:286px">CONTACT <em>INFORMATION</em></h3>
  <span class="footer-rule" style="left:286px;width:245px"></span>
  <div class="contact-info">
    <strong>Tarnwick Professional Services</strong>
    Lorem ipsum dolor sit amet,<br>consectetuer, NC1234
    <div style="height:10px"></div>
    <div class="contact-line"><svg width="12" height="12" viewBox="0 0 24 24"><path fill="#ddd" d="M6.6 10.8a15 15 0 0 0 6.6 6.6l2.2-2.2a1 1 0 0 1 1-.25 11.4 11.4 0 0 0 3.6.57 1 1 0 0 1 1 1V20a1 1 0 0 1-1 1A17 17 0 0 1 3 4a1 1 0 0 1 1-1h3.5a1 1 0 0 1 1 1c0 1.25.2 2.45.57 3.57a1 1 0 0 1-.25 1z"/></svg>(555) 014-2290</div>
    <div class="contact-line"><svg width="12" height="12" viewBox="0 0 24 24"><path fill="#ddd" d="M6 2h12v5H6zM3 8h18v9h-3v5H6v-5H3zm5 7v5h8v-5z"/></svg>(555) 014-2290</div>
    <div class="contact-line"><svg width="12" height="10" viewBox="0 0 24 18"><path fill="#ddd" d="M0 0h24v18H0zm2 2v1l10 7 10-7V2z"/></svg>info@tarnwickpro.example</div>
  </div>

  <h3 class="footer-head" style="left:579px">LOCATION <em>MAP</em></h3>
  <span class="footer-rule" style="left:579px;width:299px"></span>
  <div class="map" role="img" aria-label="Street map showing the office location with a red pin"></div>

  <div class="footer-brand">
    <div class="mark"></div>
    <div class="name">Tarnwick<br>Professional Services</div>
    <div class="footer-socials"><span></span><span></span><span></span></div>
  </div>
</footer>
<div class="copyright">Copyright © 2017. Tarnwick Professional Services. All Right Reserved</div>

</body>
</html>
```